Wedding Expo Banner Design

We are looking for four banner designs for our teeth whitening company, which is to be advertised at an upcoming wedding expo. These banners need to be eye-catching and attention grabbing, yet simple and elegant. We do not want the banners to look cluttered or overcrowded.
Feel free to incorporate relevant stock images into the design. If you do so, please include a link to the original graphics.

I have included some graphics from a competitor's website that I really love. Use them as a general guideline. I don't want you to copy these, but your designs should be inspired by them. We specifically like the pink wispy backgrounds and would like something similar to this but in our company colour.

There will be 2 portrait and 2 landscape banners.

Portrait banner 1:
1817 x 762mm Expo sign which will have a image of pretty European woman smiling with a few statements to emphasise how having a white smile can make you feel:

Look younger and healthier,
Boost confidence,
Improve appearance.
With Lumora Grin.

Portrait banner 2:
1817 x 762 mm sign which we would like to have a modern bride in her wedding dress smiling with a statement such as “Don’t be afraid to smile on your special day” or “You wouldn’t wear a stained dress, so why is your smile any different?”, “Talk to Lumora Grin now.”
If you can think of something that would advertise our brand and service better please feel free to incorporate this into your design.

Landscape banner 1 & 2:
1817 x 762mm signs which will be on the wall of the expo stand. Attached is a landscape banner from one of our competitors which we really like and would like something similar, as mentioned before we like the pink wispy background and would like this incorporated into our designs. This will be one of the first things that people at the expo see so it is really important that this sign tells people who we are and what we do- Teeth Whitening!

Both banners need to be similar in design but with different pictures and statements (however both need to say “Lumora Grin Teeth Whitening”).
“You can have the perfect smile” or “Your best smile in only 1 hour” “Ready for a smile makeover?” along with “Lumora Grin Teeth Whitening”.

Target Market(s)

20-39 year old male & females

Industry/Entity Type

Landscape

Requirements
Must have
• Both landscape banners need to be similar in design but with different pictures and statements (however both need to say “Lumora Grin Teeth Whitening”).
Should not have
• We do not want the banners to look cluttered or overcrowded.

```html
<!DOCTYPE html>
<html lang="en">
<head>
<meta charset="utf-8">
<title>Lumora Grin – Wedding Expo Banners</title>
<link rel="stylesheet" href="https://fonts.googleapis.com/css2?family=Mulish:wght@300;400;600;700;800&display=swap">
<style>
  :root {
    --page: #ffffff;
    --frame: #d4d4d4;
    --text-grey: #6f6f6f;
    --text-dark: #555555;
    --brand-navy: #1c4a86;
    --wave-deep: #1d56a8;
    --wave-mid: #4f8fd6;
    --wave-light: #bfe0f6;
    --label: #111111;
  }
  * { margin: 0; padding: 0; box-sizing: border-box; }
  html, body { width: 1200px; height: 2585px; overflow: hidden; background: var(--page); }
  body { position: relative; font-family: "Mulish", sans-serif; }

  .banner {
    position: absolute; left: 32px; width: 1149px; height: 482px;
    border: 2px solid var(--frame); background: var(--page); overflow: hidden;
  }
  .banner--youthful { top: 32px; }
  .banner--bride { top: 696px; }
  .banner--whitening { top: 1404px; }
  .banner--makeover { top: 2002px; }

  .size-label {
    position: absolute; left: 32px; font-size: 29px; font-weight: 400; color: var(--label);
  }
  .size-label--1 { top: 536px; }
  .size-label--2 { top: 1202px; }
  .size-label--3 { top: 1905px; }
  .size-label--4 { top: 2505px; }

  .waves { position: absolute; inset: 0; width: 100%; height: 100%; }

  .photo { position: absolute; }
  .photo--woman {
    right: 0; top: 0; width: 440px; height: 482px;
    background: radial-gradient(ellipse at 55% 40%, #e6c3ad 0%, #c99a80 35%, #6b4a3c 70%, rgba(255,255,255,0) 100%);
  }
  .photo--bride {
    left: 660px; top: 0; width: 430px; height: 482px;
    background: radial-gradient(ellipse at 60% 35%, #f1d7c6 0%, #e2b79f 30%, #c9a77a 50%, rgba(255,255,255,0) 75%),
                radial-gradient(circle at 25% 80%, #e0588c 0%, #e0588c 18%, rgba(255,255,255,0) 40%);
  }
  .photo--round {
    border-radius: 50%;
    box-shadow: 0 34px 22px -24px rgba(0,0,0,0.25);
  }
  .photo--teeth {
    left: 15px; top: 122px; width: 228px; height: 228px;
    background: radial-gradient(circle at 50% 45%, #ffffff 0%, #f3dede 30%, #e39c9c 60%, #f2d3d0 100%);
  }
  .photo--face {
    left: 21px; top: 55px; width: 236px; height: 236px;
    background: radial-gradient(circle at 50% 45%, #f7e3d2 0%, #e9c2a5 45%, #b98e6c 80%, #9c7a5c 100%);
  }

  .message { position: absolute; color: var(--text-grey); font-weight: 300; }
  .message strong { font-weight: 600; color: var(--text-dark); }
  .message--youthful { left: 38px; top: 56px; font-size: 37px; line-height: 45px; }
  .message--bride { left: 38px; top: 100px; font-size: 32px; line-height: 45px; }
  .message--whitening { left: 288px; top: 150px; font-size: 45px; line-height: 58px; }
  .message--whitening .headline { font-weight: 400; }
  .message--makeover { left: 283px; top: 108px; font-size: 48px; line-height: 60px; }
  .message--makeover .headline { font-weight: 400; }

  .brand {
    position: absolute; display: flex; align-items: center; gap: 14px;
    font-weight: 800; font-size: 60px; color: var(--brand-navy); letter-spacing: -0.5px;
  }
  .brand__dot { width: 22px; height: 22px; border-radius: 50%; background: var(--brand-navy); }
  .brand--youthful { left: 48px; top: 350px; }
  .brand--bride { left: 48px; top: 372px; }
  .brand--whitening { left: 585px; top: 336px; }
  .brand--makeover { left: 585px; top: 287px; }
</style>
</head>
<body>

<section class="banner banner--youthful">
  <svg class="waves" viewBox="0 0 1149 482" preserveAspectRatio="none" aria-hidden="true">
    <defs>
      <linearGradient id="wave-a" x1="0" y1="0" x2="1" y2="0">
        <stop offset="0" stop-color="#ffffff" stop-opacity="0"/>
        <stop offset="0.5" stop-color="var(--wave-mid)"/>
        <stop offset="1" stop-color="var(--wave-deep)"/>
      </linearGradient>
    </defs>
    <path d="M560 482 C700 330 900 200 1149 150 L1149 250 C950 300 780 400 700 482 Z" fill="url(#wave-a)"/>
    <path d="M620 482 C760 380 950 300 1149 290 L1149 330 C960 350 800 420 720 482 Z" fill="var(--wave-light)" opacity="0.8"/>
    <path d="M740 60 C880 110 1000 130 1149 100 L1149 120 C1000 160 880 140 740 60 Z" fill="var(--wave-mid)" opacity="0.6"/>
  </svg>
  <div class="photo photo--woman" role="img" aria-label="Photo of a smiling young woman with a bright white smile"></div>
  <p class="message message--youthful">
    Look <strong>younger</strong> and <strong>healthier</strong>,<br>
    Boost confidence,<br>
    Improve appearance.<br>
    <strong>With Lumora Grin.</strong>
  </p>
  <div class="brand brand--youthful"><span class="brand__dot"></span>Lumora Grin</div>
</section>
<p class="size-label size-label--1">1817 x 762 mm</p>

<section class="banner banner--bride">
  <svg class="waves" viewBox="0 0 1149 482" preserveAspectRatio="none" aria-hidden="true">
    <defs>
      <linearGradient id="wave-b" x1="0" y1="0" x2="1" y2="0">
        <stop offset="0" stop-color="var(--wave-light)" stop-opacity="0.3"/>
        <stop offset="0.6" stop-color="var(--wave-mid)"/>
        <stop offset="1" stop-color="var(--wave-deep)"/>
      </linearGradient>
    </defs>
    <path d="M0 0 L1149 0 L1149 70 C900 20 600 100 300 70 C180 58 80 30 0 20 Z" fill="url(#wave-b)"/>
    <path d="M0 40 C200 90 500 120 800 80 C950 60 1060 40 1149 55 L1149 70 C1050 60 950 85 800 100 C500 135 200 110 0 55 Z" fill="var(--wave-light)" opacity="0.7"/>
  </svg>
  <div class="photo photo--bride" role="img" aria-label="Photo of a smiling bride holding a bouquet of pink roses"></div>
  <p class="message message--bride">
    Don’t be afraid to smile on your<br>
    special day” or “You wouldn’t<br>
    wear a stained dress, so why is<br>
    your smile any different?”,<br>
    “Talk to Lumora Grin now.”
  </p>
  <div class="brand brand--bride"><span class="brand__dot"></span>Lumora Grin</div>
</section>
<p class="size-label size-label--2">1817 x 762 mm</p>

<section class="banner banner--whitening">
  <svg class="waves" viewBox="0 0 1149 482" preserveAspectRatio="none" aria-hidden="true">
    <defs>
      <linearGradient id="wave-c" x1="0" y1="0" x2="1" y2="0">
        <stop offset="0" stop-color="var(--wave-deep)"/>
        <stop offset="0.5" stop-color="var(--wave-mid)"/>
        <stop offset="1" stop-color="var(--wave-deep)"/>
      </linearGradient>
    </defs>
    <path d="M0 0 L1149 0 L1149 60 C950 20 800 90 600 80 C380 70 200 10 0 40 Z" fill="url(#wave-c)"/>
    <path d="M0 55 C200 25 400 90 620 100 C820 110 980 50 1149 80 L1149 95 C980 70 820 130 620 120 C400 110 200 50 0 70 Z" fill="var(--wave-light)" opacity="0.8"/>
  </svg>
  <div class="photo photo--round photo--teeth" role="img" aria-label="Close-up photo of a white smile with a dental mirror"></div>
  <p class="message message--whitening">
    <span class="headline">Lumora Grin Teeth Whitening</span><br>
    Your best smile in only 1 hour
  </p>
  <div class="brand brand--whitening"><span class="brand__dot"></span>Lumora Grin</div>
</section>
<p class="size-label size-label--3">1817 x 762 mm</p>

<section class="banner banner--makeover">
  <svg class="waves" viewBox="0 0 1149 482" preserveAspectRatio="none" aria-hidden="true">
    <defs>
      <linearGradient id="wave-d" x1="0" y1="0" x2="1" y2="0">
        <stop offset="0" stop-color="var(--wave-deep)"/>
        <stop offset="0.5" stop-color="var(--wave-mid)"/>
        <stop offset="1" stop-color="var(--wave-deep)"/>
      </linearGradient>
    </defs>
    <path d="M0 430 C250 400 500 440 750 445 C950 450 1060 420 1149 400 L1149 482 L0 482 Z" fill="url(#wave-d)"/>
    <path d="M0 405 C250 385 500 420 760 425 C950 428 1060 400 1149 385 L1149 398 C1060 415 950 440 760 438 C500 435 250 400 0 420 Z" fill="var(--wave-light)" opacity="0.8"/>
  </svg>
  <div class="photo photo--round photo--face" role="img" aria-label="Photo of a smiling woman framing her face with her hands"></div>
  <p class="message message--makeover">
    <span class="headline">Ready for a smile makeover?</span><br>
    Lumora Grin Teeth Whitening
  </p>
  <div class="brand brand--makeover"><span class="brand__dot"></span>Lumora Grin</div>
</section>
<p class="size-label size-label--4">1817 x 762 mm</p>

</body>
</html>
```